Stationary Design needed for luxorious bespoke tailor

We need a design for our stationary items like businescards, letters, envelope and letter head / Signature for email. Our company "VELMARDO" sells exclusively and luxourious bespoke garments and accessories for men. The desgins of letterhead, envelope and business card shoulderstand communicate luxury, high quality and good taste. We would like our logo to be used on the designs.

Target Market(s)

Gentleman with a high aproach and exclusive and luxourious suits and shirts, grooms, businesman,

Industry/Entity Type

It Company

Font styles to use
Sans Serif

Colors
ec1f27
ffffff

Requirements
Must have
• Logo, Companies name and adress, contactName internet & email, phone number line / mobile, VAT Nr. On Business Card frontpage only logo and name, adress companies on backpage. No VAT and Companies ID there. Company data; VELMARDO AG Sonnwiesweg 27 4068 Basel Switzerland VAT: CHE 472 916 503 Tax Tel 41 61 508 37 14 Mobile 41 79 842 07 91 www.velmardo.ch info@velmardo.com.
Nice to have
• -Name And phone numbers need to be able to change (for different coworkers ...)
Should not have
• no VAT in Business Card

```html
<!DOCTYPE html>
<html lang="en">
<head>
<meta charset="utf-8">
<title>VELMARDO AG – Stationery</title>
<link href="https://fonts.googleapis.com/css2?family=Montserrat:wght@400;500;600&display=swap" rel="stylesheet">
<style>
  :root {
    --red: #ec1f27;
    --black: #000000;
    --white: #ffffff;
    --ink: #111111;
    --backdrop: #e4e4e4;
  }
  * { margin: 0; padding: 0; box-sizing: border-box; }
  html, body { width: 1200px; height: 923px; overflow: hidden; background: var(--backdrop); }
  body { position: relative; font-family: "Montserrat", Arial, sans-serif; color: var(--ink); }

  .sheet { position: absolute; background: var(--white); overflow: hidden; }
  .letterhead { left: 60px; top: 29px; width: 669px; height: 865px; }
  .card-front { left: 853px; top: 29px; width: 241px; height: 422px; }
  .card-back { left: 853px; top: 471px; width: 241px; height: 423px; background: var(--black); }

  .brand-name {
    position: absolute; left: 0; right: 0; text-align: center;
    font-weight: 600; color: var(--black); line-height: 1; transform: translateY(-50%);
  }
  .letterhead .brand-name { top: 56px; font-size: 40px; letter-spacing: 3px; }
  .card-front .brand-name { top: 56px; font-size: 24px; letter-spacing: 2px; }
  .card-back .brand-name { top: 210px; font-size: 24px; letter-spacing: 2px; color: var(--white); }

  .rule { position: absolute; left: 0; right: 0; top: 711px; height: 1px; background: var(--red); }

  .contact-line {
    position: absolute; left: 0; right: 0; text-align: center; white-space: nowrap;
    line-height: 1; transform: translateY(-50%); color: var(--ink);
  }
  .letterhead .contact-line { font-size: 9.5px; }
  .card-front .contact-line { font-size: 11px; }
  .label { color: var(--red); }
  .red { color: var(--red); }

  .company-title {
    position: absolute; left: 0; right: 0; top: 255px; transform: translateY(-50%);
    text-align: center; font-size: 18px; font-weight: 600; color: var(--red); line-height: 1;
  }
  .side-bar { position: absolute; top: 249px; width: 36px; height: 12px; background: var(--black); }
  .side-bar.left { left: 0; }
  .side-bar.right { right: 0; }

  .footer-band { position: absolute; left: 0; width: 100%; display: block; }
  .letterhead .footer-band { top: 816px; height: 49px; }
  .card-front .footer-band { top: 405px; height: 17px; }
  .card-back .footer-band { top: 405px; height: 18px; }
</style>
</head>
<body>

<section class="sheet letterhead" aria-label="Letterhead">
  <div class="brand-name">VELMARDO</div>
  <div class="rule"></div>
  <p class="contact-line" style="top:725px">Sonnwiesweg 27 4068</p>
  <p class="contact-line" style="top:737px">Basel Switzerland</p>
  <p class="contact-line" style="top:751px"><span class="label">VAT: CHE</span> 472 916 503 TAX</p>
  <p class="contact-line" style="top:768px"><span class="label">P:</span> 41 61 508 37 14</p>
  <p class="contact-line" style="top:780px"><span class="label">M:</span> 41 79 842 07 91</p>
  <p class="contact-line" style="top:791px"><span class="label">E:</span> info@velmardo.com</p>
  <p class="contact-line" style="top:802px"><span class="label">W:</span> www.<span class="red">velmardo</span>.ch</p>
  <svg class="footer-band" viewBox="0 0 786 57" preserveAspectRatio="none" aria-hidden="true">
    <polygon points="0,0 497,0 440,57 0,57" fill="var(--black)"/>
    <polygon points="505,0 786,0 786,57 450,57" fill="var(--red)"/>
  </svg>
</section>

<section class="sheet card-front" aria-label="Business card front">
  <div class="brand-name">VELMARDO</div>
  <div class="side-bar left"></div>
  <div class="side-bar right"></div>
  <h1 class="company-title">VELMARDO AG</h1>
  <p class="contact-line" style="top:278px">Sonnwiesweg 27 4068</p>
  <p class="contact-line" style="top:292px">Basel Switzerland</p>
  <p class="contact-line" style="top:312px"><span class="label">P:</span> 41 61 508 37 14</p>
  <p class="contact-line" style="top:325px"><span class="label">M:</span> 41 79 842 07 91</p>
  <p class="contact-line" style="top:338px"><span class="label">E:</span> info@velmardo.com</p>
  <p class="contact-line" style="top:351px"><span class="label">W:</span> www.<span class="red">velmardo</span>.ch</p>
  <svg class="footer-band" viewBox="0 0 284 20" preserveAspectRatio="none" aria-hidden="true">
    <polygon points="0,0 155,0 137,20 0,20" fill="var(--black)"/>
    <polygon points="157,0 284,0 284,20 139,20" fill="var(--red)"/>
  </svg>
</section>

<section class="sheet card-back" aria-label="Business card back">
  <div class="brand-name">VELMARDO</div>
  <svg class="footer-band" viewBox="0 0 284 21" preserveAspectRatio="none" aria-hidden="true">
    <polygon points="0,0 155,0 135,21 0,21" fill="var(--white)"/>
    <polygon points="158,0 284,0 284,21 138,21" fill="var(--red)"/>
  </svg>
</section>

</body>
</html>
```